Work Start DL brochure

I need a design for a double sided card and 6 page flyer to hand out to students to promote our Brightpath Work Start Program. It is an 8 week program that gives budding Accountants exposure to real-life case studies in Bookkeeping & Accounting. The design for the business cards we give students at completion of the program is done. I would like some DL cards and a 6 page brochure to match the business card design. I want a template so I can just add the text I need. I have attached a sample 6 page brochure I use for employers and the business cards we use for students (2 different markets). Make sure your design matches the look of the business cards.
Updates

Reason: So far I only have one designer and I need a few more. I would prefer to work with a designer who has looked at the business card that I uploaded and come up with a design which incorporates the colours, the look and feel. Once this is agreed, the DL brochure can be done quickly I would imagine. The DL card will have very little text and will be more about design with a short message, It will be used as a Mail Out to send out in the mail to capture interest in the program.

I have extended the deadline by 24 hours due to the lack of responses. If you intend making a submission but cannot meet the deadline, please let me know at marelt@brightpathqv.com.au I am looking for a good design which matches our business card (uploaded in the brief), please do not just put all the photos at the top of every page and leave the text in a boring font with little thought to the layout. I am looking for something different. That is why I have not gone to a printer who will just dump my text straight into someone elses template. If I find a designer with a bit of spark, I am happy to guide you through until it is right. Due to the time restrictions now, I will close the applications once I find the right designer. I don't want 10 designers, I only want 1 or 2 good ones and I happy to pay a fee for second prize, or work with them exclusively on another project. The colours are already there, this should be a fairly straight forward job. I think also, the business cards are very bold, the brochure should be less bold but still be obvious that it follows the same design.

Target Market(s)

Accounting Graduates currently studying and those employed but working in non-financial jobs. Looking for work experience so they can get their foot in the door.

Industry/Entity Type

Business

Requirements
Must have
• Matching design to the attached business cards. Must be creative. Include both DL and brochure layout.
Should not have
• The attached brochure is a sample of our Employer brochure, this should be different to the student brochure in this new design.

```html
<!DOCTYPE html>
<html lang="en">
<head>
<meta charset="utf-8">
<title>Brightpath Work Start Program – DL Brochure</title>
<link href="https://fonts.googleapis.com/css2?family=Lato:wght@400;700;900&display=swap" rel="stylesheet">
<style>
  :root {
    --navy: #0d4a6e;
    --green: #8dc63f;
    --text: #6b6b6b;
    --bg-top: #ffffff;
    --bg-bottom: #ececec;
    --white: #ffffff;
  }
  html, body {
    margin: 0;
    padding: 0;
    overflow: hidden;
  }
  .brochure {
    position: relative;
    width: 1200px;
    height: 848px;
    overflow: hidden;
    background: linear-gradient(180deg, var(--bg-top) 0%, #f6f6f6 45%, var(--bg-bottom) 100%);
    font-family: "Lato", Arial, sans-serif;
    color: var(--text);
  }
  .shapes {
    position: absolute;
    left: 0;
    top: 0;
  }
  .section-title {
    position: absolute;
    height: 42px;
    margin: 0;
    display: flex;
    align-items: center;
    padding-left: 14px;
    box-sizing: border-box;
    color: var(--white);
    font-weight: 700;
    font-size: 14.5px;
    letter-spacing: 0.1px;
    text-transform: uppercase;
    white-space: nowrap;
  }
  .section-title.navy { background: var(--navy); }
  .section-title.green { background: var(--green); }
  .section-title.edge { border-radius: 0 10px 10px 0; }
  .section-title.round { border-radius: 10px; }
  .copy {
    position: absolute;
    margin: 0;
    font-size: 13px;
    line-height: 19.5px;
    text-align: justify;
  }
  .points {
    position: absolute;
    margin: 0;
    padding: 0;
    list-style: none;
    font-size: 13px;
    line-height: 21px;
  }
  .points li::before {
    content: "";
    display: inline-block;
    width: 4px;
    height: 4px;
    border-radius: 50%;
    background: var(--green);
    margin-right: 5px;
    vertical-align: middle;
    position: relative;
    top: -3px;
  }
  .brand-name {
    position: absolute;
    left: 880px;
    top: 705px;
    display: flex;
    align-items: center;
    gap: 10px;
    color: var(--navy);
    font-weight: 900;
    font-size: 27px;
    white-space: nowrap;
  }
  .brand-mark {
    width: 22px;
    height: 22px;
    border-radius: 50%;
    background: var(--green);
  }
  .web-address {
    position: absolute;
    left: 832px;
    top: 801px;
    margin: 0;
    color: var(--navy);
    font-weight: 900;
    font-size: 21.5px;
  }
</style>
</head>
<body>
<main class="brochure">

  <svg class="shapes" width="1200" height="848" viewBox="0 0 1200 848">
    <defs>
      <linearGradient id="photo-office" x1="0" y1="0" x2="1" y2="1">
        <stop offset="0" stop-color="#e6eef4"/>
        <stop offset="0.5" stop-color="#c9b6a6"/>
        <stop offset="1" stop-color="#8fa2b3"/>
      </linearGradient>
      <linearGradient id="photo-group" x1="0" y1="0" x2="1" y2="1">
        <stop offset="0" stop-color="#f1eee6"/>
        <stop offset="0.55" stop-color="#b7c4a0"/>
        <stop offset="1" stop-color="#8a6a55"/>
      </linearGradient>
      <linearGradient id="photo-friends" x1="0" y1="0" x2="0" y2="1">
        <stop offset="0" stop-color="#b9d6ee"/>
        <stop offset="0.5" stop-color="#d6a98c"/>
        <stop offset="1" stop-color="#5b7fae"/>
      </linearGradient>
      <filter id="card-shadow" x="-10%" y="-20%" width="130%" height="150%">
        <feDropShadow dx="0" dy="3" stdDeviation="4" flood-color="#000" flood-opacity="0.22"/>
      </filter>
    </defs>

    <g role="img" aria-label="Photo of young colleagues working together at a computer in an office">
      <path d="M-6,184 H322 Q341,184 347,201 L385,368 Q389,389 367,389 H-6 Z"
            fill="url(#photo-office)" stroke="var(--green)" stroke-width="6"/>
    </g>

    <g role="img" aria-label="Photo of a smiling student standing in front of a group of people">
      <path d="M1206,184 H878 Q859,184 853,201 L807,368 Q803,389 825,389 H1206 Z"
            fill="url(#photo-group)" stroke="var(--green)" stroke-width="6"/>
    </g>

    <g role="img" aria-label="Photo of a group of smiling young friends outdoors">
      <path d="M400,564 H690 Q711,564 719,583 L798,799 Q804,820 782,820 H400 Z"
            fill="url(#photo-friends)" stroke="var(--green)" stroke-width="6"/>
    </g>

    <path d="M878,680 H1206 V773 H856 Q838,773 842,757 L858,695 Q862,680 878,680 Z"
          fill="var(--white)" filter="url(#card-shadow)"/>
  </svg>

  <!-- Left panel -->
  <h2 class="section-title navy edge" style="left:0; top:33px; width:368px;">Vivamus massa massa, tempor et leo eget</h2>
  <p class="copy" style="left:13px; top:87px; width:347px;">Etiam ultrices sodales tellus, et imperdiet lorem viverra sit amet. Morbi convallis vitae nunc et tempus. Quisque accumsan</p>

  <p class="copy" style="left:13px; top:423px; width:347px;">Etiam ultrices sodales tellus, et imperdiet lorem viverra sit amet. Morbi convallis vitae nunc et tempus. Quisque accumsan metus nunc, iaculis blandit arcu suscipit nec. Sed rutrum libero non</p>

  <h2 class="section-title green edge" style="left:0; top:565px; width:370px;">Vivamus massa massa, tempor et leo eget</h2>
  <p class="copy" style="left:13px; top:617px; width:347px;">Sodales tellus, et imperdiet lorem viverra sit amet. Morbi convallis vitae nunc et tempus.</p>
  <ul class="points" style="left:13px; top:673px;">
    <li>Quisque accumsan metus nunc</li>
    <li>Laculis blandit arcu suscipit nec</li>
    <li>Sed rutrum libero non</li>
    <li>Vitae nunc et tempus.</li>
    <li>Lorem viverra sit amet.</li>
  </ul>

  <!-- Middle panel -->
  <h2 class="section-title green round" style="left:397px; top:33px; width:370px;">Vivamus massa massa, tempor et leo eget</h2>
  <p class="copy" style="left:413px; top:88px; width:347px;">Sodales tellus, et imperdiet lorem viverra sit amet. Morbi convallis vitae nunc et tempus.</p>
  <ul class="points" style="left:413px; top:144px;">
    <li>Quisque accumsan metus nunc</li>
    <li>Laculis blandit arcu suscipit nec</li>
    <li>Sed rutrum libero non</li>
    <li>Vitae nunc et tempus.</li>
    <li>Lorem viverra sit amet.</li>
  </ul>

  <h2 class="section-title navy round" style="left:397px; top:317px; width:370px;">Vivamus massa massa, tempor et leo eget</h2>
  <p class="copy" style="left:413px; top:381px; width:347px;">Etiam ultrices sodales tellus, et imperdiet lorem viverra sit amet. Morbi convallis vitae nunc et tempus. Quisque accumsan metus nunc, iaculis blandit arcu suscipit nec. Sed rutrum libero non</p>
  <ul class="points" style="left:413px; top:466px;">
    <li>Sed rutrum libero non</li>
    <li>Vitae nunc et tempus.</li>
    <li>Lorem viverra sit amet.</li>
  </ul>

  <!-- Right panel -->
  <h2 class="section-title navy edge" style="left:800px; top:33px; width:369px;">Vivamus massa massa, tempor et leo eget</h2>
  <p class="copy" style="left:815px; top:87px; width:347px;">Etiam ultrices sodales tellus, et imperdiet lorem viverra sit amet. Morbi convallis vitae nunc et tempus. Quisque accumsan metus nunc.</p>

  <h2 class="section-title green edge" style="left:800px; top:431px; width:371px;">Vivamus massa massa, tempor et leo eget</h2>
  <p class="copy" style="left:820px; top:485px; width:347px;">Etiam ultrices sodales tellus, et imperdiet lorem viverra sit amet. Morbi convallis vitae nunc et tempus. Quisque accumsan metus nunc, iaculis blandit arcu suscipit nec. Sed rutrum libero non</p>
  <ul class="points" style="left:820px; top:570px;">
    <li>Sed rutrum libero non</li>
    <li>Vitae nunc et tempus.</li>
    <li>Lorem viverra sit amet.</li>
  </ul>

  <div class="brand-name"><span class="brand-mark"></span>Brightpath Work Start</div>
  <p class="web-address">www.BrightpathWorkStart.com.au</p>

</main>
</body>
</html>
```